Flyer für Vermietung von Baumaschinen und Werkzeugen
Zielgruppe
Vermietung von Baumaschinen und Werkzeugen, sowie der Verkauf von Baustoffen /-materialien
Aufgabenstellung
Ich hätte gerne einen Flyer in Din A5 oder Din A6. Auf einer Seite soll Werbung für die Vermietung gemacht werden, auf der anderen Werbung für den Verkauf.
Das Logo zur Einbindung wird nachgeliefert.
Es soll ein Vermerk auf den Flyer, 'Jetzt neu bei Heidelberg-Leimen'
Auch soll die Adresse mit auf den flyer: www.leihfalke.de
Als Farbe bitte grüntöne verwenden

```html
<!DOCTYPE html>
<html lang="de">
<head>
<meta charset="utf-8">
<title>Flyer – Vermietung von Baumaschinen und Werkzeugen</title>
<link href="https://fonts.googleapis.com/css2?family=Courgette&family=Arimo:wght@400;700&display=swap" rel="stylesheet">
<style>
  :root {
    --frame-green: #009a00;
    --panel-green: #5abb4a;
    --frame-white: #ffffff;
    --headline-orange: #ff6a13;
    --text-white: #ffffff;
    --placeholder-grey: #e6e6e6;
    --sky: #a9c6e6;
    --machine: #e0a52a;
    --earth: #8a6e52;
  }
  html, body {
    margin: 0;
    padding: 0;
    width: 845px;
    height: 1200px;
    overflow: hidden;
    background: #ffffff;
  }
  .flyer {
    position: relative;
    width: 845px;
    height: 1200px;
    overflow: hidden;
    font-family: "Arimo", Arial, sans-serif;
  }
  .flyer-frame {
    position: absolute;
    inset: 0;
  }
  .hero-photo {
    position: absolute;
    left: 45px;
    top: 308px;
    width: 758px;
    height: 494px;
    background: linear-gradient(180deg, var(--sky) 0%, #c9d9e9 30%, var(--machine) 55%, #a48466 75%, var(--earth) 100%);
  }
  .headline {
    position: absolute;
    left: 0;
    top: 0;
    width: 845px;
    height: 420px;
  }
  .headline text {
    font-family: "Courgette", cursive;
    fill: var(--headline-orange);
    stroke: var(--frame-white);
    stroke-width: 2;
    paint-order: stroke;
  }
  .logo-placeholder {
    position: absolute;
    left: 590px;
    top: 83px;
    width: 182px;
    height: 182px;
    border: 2px solid #000;
    border-radius: 50%;
    background: #fff;
    display: flex;
    flex-direction: column;
    justify-content: center;
    align-items: center;
    transform: rotate(-18deg);
    color: var(--placeholder-grey);
    font-weight: 700;
    font-size: 24px;
    line-height: 1.4;
  }
  .tagline {
    position: absolute;
    left: 108px;
    top: 803px;
    margin: 0;
    color: var(--text-white);
    font-weight: 700;
    font-size: 25px;
  }
  .contact {
    position: absolute;
    color: var(--text-white);
    font-weight: 700;
    font-size: 25px;
    line-height: 49px;
    margin: 0;
  }
  .contact-address { left: 107px; top: 893px; }
  .contact-reach { left: 379px; top: 893px; }
  .website {
    position: absolute;
    left: 0;
    width: 845px;
    top: 1043px;
    text-align: center;
    color: var(--text-white);
    font-size: 22px;
  }
</style>
</head>
<body>
<div class="flyer">
  <svg class="flyer-frame" width="845" height="1200" viewBox="0 0 845 1200">
    <rect width="845" height="1200" fill="var(--frame-green)"/>
    <polygon fill="var(--frame-white)" points="75,32 772,32 813,75 813,1125 772,1168 75,1168 33,1125 33,75"/>
    <polygon fill="var(--panel-green)" points="82,45 765,45 803,82 803,1118 765,1155 82,1155 45,1118 45,82"/>
  </svg>

  <div class="hero-photo" role="img" aria-label="Foto: gelbe Planierraupe mit Fahrer auf einer Baustelle, dahinter Seilbagger vor blauem Himmel"></div>

  <svg class="headline" viewBox="0 0 845 420" aria-label="Jetzt neu bei Heidelberg-Leimen">
    <defs>
      <path id="arc-town" d="M160,355 Q420,170 710,375"/>
    </defs>
    <text x="385" y="140" font-size="66" text-anchor="middle" transform="rotate(-8 385 140)" letter-spacing="4">Jetzt neu</text>
    <text x="388" y="205" font-size="62" text-anchor="middle" transform="rotate(-6 388 205)" letter-spacing="4">bei</text>
    <text font-size="52" letter-spacing="7">
      <textPath href="#arc-town" startOffset="0">Heidelberg-Leimen</textPath>
    </text>
  </svg>

  <div class="logo-placeholder"><span>Logo</span><span>Platzhalter</span></div>

  <p class="tagline">Vermietung von Baumaschinen und Werkzeugen</p>

  <p class="contact contact-address">Firma XXX<br>Musterstraße 11<br>12345 Musterhausen</p>
  <p class="contact contact-reach">Tel: XXXXXXX<br>Email: xxxxxxxx</p>

  <div class="website">www.leihfalke.de</div>
</div>
</body>
</html>
```